Business Card 85x40mm - Freelance audio mixing / live event operator

I am a freelance audio operator working in live events. Mostly corporate events mixing sound for a range of entertainment, awards nights and functions. I need a new card to give to perspective clients.

The final design will convey bold professionalism with a general dark vibe. Looking for dark-ish background with some smatterings of colour added.

I have attatched my old BC for an idea of what I have liked in the past. Id like a more modern updated design (that circular design on the back is not my logo it is just a picture I found that resembled sound} . For an added element possibly a mixture of some playful colours in a way that resembles an audio wave form or sound.

I have attached a photo called "audio software" with some colourful squiggly lines; maybe incorporate elements of that into into design
Updates

Added extra $ to project Damn Pixel hives fees are unreasonable

Target Market(s)

Mostly corporate clients

Industry/Entity Type

Events

Contact Information for Business Card

Corwin Pellath
Sound | FOH | Monitors | Systems | Corporate

Digital Audio Mixing Specialist, Live Event Technical Professional,

corwinpellath@mailvexo.net, +61 402 918 357

Colors
ec1f27
ffc214
9bcb3c
6b449b

Requirements
Must have
• Dark theme
• 85x40mm dimensions
Nice to have
• some sort of imagery or design to reflect audio/sound

```html
<!DOCTYPE html>
<html lang="en">
<head>
<meta charset="utf-8">
<title>Corwin Pellath – Business Card</title>
<link rel="stylesheet" href="https://fonts.googleapis.com/css2?family=Audiowide&family=Ubuntu:wght@400;500&display=swap">
<style>
  :root {
    --backdrop: #252728;
    --card: #2a2a2b;
    --accent: #f3b928;
    --text-light: #f2f2f2;
    --text-dark: #2a2a2b;
  }
  html, body {
    margin: 0;
    padding: 0;
    width: 1200px;
    height: 1000px;
    overflow: hidden;
    background: var(--backdrop);
  }
  .canvas {
    position: relative;
    width: 1200px;
    height: 1000px;
    font-family: "Ubuntu", sans-serif;
    color: var(--text-light);
  }
  .card {
    position: absolute;
    left: 297px;
    width: 607px;
    height: 286px;
    background: var(--card);
  }
  .card-front { top: 155px; }
  .card-back { top: 563px; }

  .front-name {
    position: absolute;
    top: 110px;
    left: 0;
    width: 100%;
    margin: 0;
    text-align: center;
    font-family: "Audiowide", sans-serif;
    font-weight: 400;
    font-size: 38px;
    letter-spacing: 2px;
    line-height: 1;
    color: var(--accent);
    text-transform: uppercase;
  }
  .front-role {
    position: absolute;
    top: 157px;
    left: 100px;
    width: 410px;
    display: flex;
    align-items: center;
    gap: 8px;
    font-size: 19px;
    font-weight: 500;
    line-height: 1;
  }
  .front-role .rule {
    flex: 1;
    height: 2px;
    background: var(--accent);
  }
  .back-contact,
  .back-services {
    position: absolute;
    left: 0;
    width: 100%;
    margin: 0;
    text-align: center;
    font-size: 15px;
    font-weight: 500;
    line-height: 1;
    word-spacing: 1px;
  }
  .back-contact { top: 32px; }
  .back-services { top: 243px; }
  .divider { padding: 0 6px; }

  .back-rule {
    position: absolute;
    left: 0;
    top: 143px;
    width: 100%;
    height: 2px;
    background: var(--accent);
  }
  .brand-badge {
    position: absolute;
    left: 235px;
    top: 76px;
    width: 136px;
    height: 136px;
  }
  .brand-name {
    position: absolute;
    left: 235px;
    top: 136px;
    width: 136px;
    text-align: center;
    font-size: 14px;
    font-weight: 500;
    line-height: 1;
    color: var(--text-dark);
  }
</style>
</head>
<body>
<main class="canvas">
  <section class="card card-front">
    <h1 class="front-name">Corwin Pellath</h1>
    <p class="front-role"><span class="rule"></span>Audio Visual Technician<span class="rule"></span></p>
  </section>

  <section class="card card-back">
    <p class="back-contact">+61 402 918 357<span class="divider">|</span>corwinpellath@mailvexo.net</p>
    <div class="back-rule"></div>
    <svg class="brand-badge" viewBox="0 0 136 136" aria-hidden="true">
      <circle cx="68" cy="68" r="62" fill="var(--card)" stroke="var(--accent)" stroke-width="2"/>
      <circle cx="68" cy="68" r="58" fill="var(--accent)"/>
    </svg>
    <span class="brand-name">Corwin Pellath</span>
    <p class="back-services">Live Digital Audio Mixing<span class="divider">|</span>Events Professional</p>
  </section>
</main>
</body>
</html>
```